Website for a mini excavator hire business
Bridgeway Plant Hire
Construction
www.bwphire.com.au
Bridgeway Plant Hire, offers affordable, fully serviced and maintained excavator hire, for long or short term periods.
We have available late model Tarvolen excavator for all your earthmoving needs.
TVL Mini Hydraulic Excavators come equipped with an aluminium trailer and 3 buckets as standard.
Perfect for builders, plumbers, electrical contractors and landscape gardeners.
Would like a modern masculine website that is simple and easy to read and navigate for our customers who are tradesman. I like the silhouette of excavators in the header image.
below header
www.kestrelhaulage.com.au
www.brannockrent.com.au
www.trenchpilot.net.au/home
Looking for a modern and crisp website design that is masculine in style and color.
Some text from the back of my business card that could be used on the front page of the website.
Regards,
Dorian Pelkaw.

```html
<!DOCTYPE html>
<html lang="en">
<head>
<meta charset="utf-8">
<title>Bridgeway Plant Hire – Mini Excavator Hire</title>
<link href="https://fonts.googleapis.com/css2?family=Arimo:wght@400;700&family=Oswald:wght@500;700&display=swap" rel="stylesheet">
<style>
:root{
  --yellow:#f2e21a;
  --black:#0d0d0d;
  --panel:#2b2b2b;
  --grey:#5a5a5a;
  --white:#ffffff;
  --sky-top:#c9e7f7;
  --sky-bottom:#5fb6e6;
  --ink:#111a22;
}
*{margin:0;padding:0;box-sizing:border-box}
html,body{width:1200px;height:1080px;overflow:hidden;background:var(--black);font-family:"Arimo",Arial,sans-serif;color:var(--white)}
.page{position:relative;width:1200px;height:1080px}

/* header */
.header{position:absolute;left:0;top:0;width:1200px;height:211px;background:linear-gradient(#111 0%,#1a1a1a 100%)}
.header-scene{position:absolute;left:500px;top:0;width:700px;height:211px;background:linear-gradient(160deg,#d9dcdd 0%,#a9adb0 45%,#3a3a3a 85%,#141414 100%)}
.brand{position:absolute;left:132px;top:48px;display:flex;align-items:center;gap:18px}
.brand-square{width:76px;height:76px;background:var(--yellow)}
.brand-name{font-family:"Oswald",sans-serif;font-weight:700;font-size:34px;line-height:38px;color:var(--yellow);text-transform:uppercase;letter-spacing:.5px;width:240px}
.brand-tag{position:absolute;left:226px;top:140px;font-weight:700;font-size:15px;color:var(--white)}
.phone-tab{position:absolute;left:865px;top:0;width:205px;height:41px;background:var(--yellow);border-radius:0 0 20px 20px;display:flex;align-items:center;justify-content:center;gap:10px;font-weight:700;font-size:17px;color:var(--black)}

/* nav */
.nav{position:absolute;left:0;top:211px;width:1200px;height:67px;background:linear-gradient(#8a8a8a,#5e5e5e 50%,#4a4a4a)}
.nav ul{position:absolute;left:120px;top:0;display:flex;list-style:none;height:67px}
.nav li{padding:0 18px;line-height:67px;font-size:14px;font-weight:700;color:var(--white);border-right:1px solid #3b3b3b;white-space:nowrap}
.nav li.active{color:var(--yellow);background:#3e3e3e}
.search{position:absolute;left:768px;top:222px;width:300px;height:40px;background:#6b6b6b;border:1px solid #7d7d7d}
.search svg{position:absolute;right:12px;top:11px}

/* hero */
.hero{position:absolute;left:0;top:278px;width:1200px;height:360px;background:linear-gradient(100deg,var(--sky-top) 0%,#8fd0f2 45%,var(--sky-bottom) 100%)}
.hero h1{position:absolute;left:138px;top:66px;font-size:20px;font-weight:700;color:var(--ink);text-transform:uppercase}
.hero p{position:absolute;left:138px;top:102px;width:460px;font-size:14.5px;line-height:17.5px;color:#2a6a96}
.btn{display:inline-block;background:var(--yellow);color:var(--black);font-weight:700;text-transform:uppercase}
.hero .btn{position:absolute;left:138px;top:243px;width:135px;height:48px;line-height:48px;text-align:center;font-size:17px}
.hero-photo{position:absolute;left:650px;top:27px;width:411px;height:310px;background:var(--white);padding:12px}
.hero-photo div{width:100%;height:100%;background:radial-gradient(ellipse at 55% 55%,#e8b83a 0%,#c7922a 35%,#f4f4f4 70%)}
.arrow{position:absolute;top:150px}

/* content */
.content{position:absolute;left:0;top:638px;width:1200px;height:372px;background:var(--black)}
.welcome{position:absolute;left:130px;top:30px;width:580px}
.welcome h2{font-size:17px;font-weight:700;text-transform:uppercase}
.welcome h2 span{color:var(--yellow)}
.rule{height:4px;background:var(--grey);margin:10px 0 20px;width:575px}
.rule::before{content:"";display:block;width:60px;height:4px;background:var(--yellow)}
.welcome h3{font-size:14.5px;font-weight:700;color:var(--yellow);text-transform:uppercase;margin-bottom:14px}
.welcome p{font-size:13.5px;line-height:18px;color:#e6e6e6}
.welcome p+p{margin-top:7px}
.price{position:absolute;left:130px;top:280px;width:575px;height:50px}
.price span{position:absolute;left:20px;top:0;line-height:50px;font-family:"Oswald",sans-serif;font-weight:500;font-size:16px;color:var(--ink);letter-spacing:.5px}
.price b{color:#c61e1e;font-size:19px}

.quick{position:absolute;left:747px;top:92px;width:323px;height:272px;background:var(--panel)}
.quick h4{height:38px;line-height:38px;background:var(--yellow);color:var(--black);text-align:center;font-size:15px;font-weight:700;text-transform:uppercase}
.field{position:absolute;height:34px;background:#111;border:1px solid #444;font-size:13px;padding:9px 10px;color:#ddd}
.field.tall{height:64px}
.quick .btn{position:absolute;left:96px;top:236px;width:130px;height:36px;line-height:36px;text-align:center;font-size:15px;border-radius:0 0 14px 14px}

/* footer */
.footer{position:absolute;left:0;top:1010px;width:1200px;height:70px;background:linear-gradient(#1e1e1e,#2a2a2a);display:flex;align-items:center;justify-content:center;gap:26px;font-size:14px;color:var(--white)}
.footer em{font-style:normal;color:var(--yellow)}
</style>
</head>
<body>
<div class="page">

  <header class="header">
    <div class="header-scene" role="img" aria-label="Silhouettes of excavators and a dump truck against a grey sky"></div>
    <div class="brand">
      <div class="brand-square"></div>
      <div class="brand-name">Bridgeway Plant Hire</div>
    </div>
    <div class="brand-tag">Get the job done for less</div>
    <div class="phone-tab">
      <svg width="18" height="18" viewBox="0 0 24 24"><path d="M6.6 10.8a15 15 0 0 0 6.6 6.6l2.2-2.2c.3-.3.7-.4 1-.2 1.1.4 2.3.6 3.6.6.6 0 1 .4 1 1V20c0 .6-.4 1-1 1A17 17 0 0 1 3 4c0-.6.4-1 1-1h3.5c.6 0 1 .4 1 1 0 1.3.2 2.5.6 3.6.1.3 0 .7-.2 1z" fill="#0d0d0d"/></svg>
      1300 - 47 - 26 - 90
    </div>
  </header>

  <nav class="nav">
    <ul>
      <li class="active">HOME</li>
      <li>ABOUT US</li>
      <li>OUR EQUIPMENT</li>
      <li>SAFETY</li>
      <li>CONTACT US</li>
    </ul>
  </nav>
  <div class="search">
    <svg width="16" height="16" viewBox="0 0 16 16"><circle cx="6.5" cy="6.5" r="4.5" stroke="#ddd" stroke-width="2" fill="none"/><line x1="10" y1="10" x2="14.5" y2="14.5" stroke="#ddd" stroke-width="2"/></svg>
  </div>

  <section class="hero">
    <h1>Pellentesque interdum eros lectus nulla</h1>
    <p>Lorem ipsum dolor sit amet, consectetur adipiscing elit. Nulla malesuada, turpis et ultricies condimentum, sem ligula pulvinar nunc, ut sagittis justo augue at dolor. Donec id placerat elus. Fusce posuere sem quis metus rutrum tristique. Nam ante libero, interdum vitae nunc sit amet, placerat feugiat diam. Duis fringilla dignissim nulla. Donec condimentum fringilla vestibulum</p>
    <span class="btn">Read more</span>
    <div class="hero-photo"><div role="img" aria-label="Yellow wheel loader with front bucket on a white background"></div></div>
    <svg class="arrow" style="left:70px" width="22" height="50" viewBox="0 0 22 50"><polyline points="18,3 4,25 18,47" fill="none" stroke="#5a98c2" stroke-width="4"/></svg>
    <svg class="arrow" style="left:1108px" width="22" height="50" viewBox="0 0 22 50"><polyline points="4,3 18,25 4,47" fill="none" stroke="#eaf6fd" stroke-width="4"/></svg>
  </section>

  <section class="content">
    <div class="welcome">
      <h2>Welcome to <span>Bridgeway Plant Hire</span></h2>
      <div class="rule"></div>
      <h3>We are Melbourne's mini excavator specialist</h3>
      <p>Bridgeway Plant Hire, based in Melbourne's North-Eastern suburbs offers affordable, fully serviced and maintained excavator hire, for long or short term periods.</p>
      <p>We have available late model Tarvolen excavators featuring buckets and augers for all your earthmoving needs.</p>
      <p>TVL Mini Hydraulic Excavators come equipped with an aluminium trailer and 3 buckets as standard. Auger attachments are also available.<br>Perfect for builders, plumbers, electrical contractors and landscape gardeners.</p>
    </div>
    <div class="price">
      <svg width="575" height="50" viewBox="0 0 575 50"><defs><linearGradient id="priceFill" x1="0" y1="0" x2="0" y2="1"><stop offset="0" stop-color="#e6e6e6"/><stop offset="1" stop-color="#a8a8a8"/></linearGradient></defs><polygon points="0,0 550,0 575,25 550,50 0,50" fill="url(#priceFill)"/></svg>
      <span>PRICE STARTING AT <b>$207</b> PER DAY (INCLUDES 3 BUCKETS, TRAILER &amp; GST)</span>
    </div>

    <form class="quick">
      <h4>Quick contact</h4>
      <div class="field" style="left:22px;top:48px;width:279px">Name</div>
      <div class="field" style="left:22px;top:92px;width:138px">Email</div>
      <div class="field" style="left:170px;top:92px;width:131px">Phone</div>
      <div class="field" style="left:22px;top:136px;width:279px">Subject</div>
      <div class="field tall" style="left:22px;top:180px;width:279px">Message</div>
      <span class="btn">Submit</span>
    </form>
  </section>

  <footer class="footer">
    <span>Copyright © 2013 <em>Bridgeway Plant Hire</em></span>
    <span>|</span><span>Privacy policy</span>
    <span>|</span><span>Terms &amp; Conditions Applied</span>
  </footer>

</div>
</body>
</html>
```